Company Business Card

I need a Business card designed for my granite company(We install and supply Granite Counter tops). It just needs to have the employee name, title, Store address, email, and phone number. With a nifty logo design and preferably our Mapvista map location on the backside. I am not creative so you can go crazy or simple on the logo.
Company Name : The Marble Depot
Employee Name: Carl Whitmore
Title: Owner
Address: 10483 Pelham Ridge Blvd. Dallas, Texas 75220
Email: Carl.Whitmore@MDPlanoworks.com
Phone: 214-555-0182

```html
<!DOCTYPE html>
<html lang="en">
<head>
<meta charset="utf-8">
<title>The Marble Depot – Business Card</title>
<link href="https://fonts.googleapis.com/css2?family=Exo+2:wght@400;500&display=swap" rel="stylesheet">
<style>
  :root {
    --page: #ecebe8;
    --card-black: #0b0b0b;
    --card-glow: #2e2e2e;
    --ink-white: #ffffff;
    --ink-soft: #cfcfcf;
    --ink-muted: #9a9a9a;
    --ink-map: #6f6d68;
    --map-fill: #e8e5de;
    --map-fill-deep: #e0ddd5;
    --marker: #2a2a2a;
  }
  * { box-sizing: border-box; margin: 0; padding: 0; }
  html, body {
    width: 1200px; height: 1000px; overflow: hidden;
    background: var(--page);
    font-family: "Exo 2", "Helvetica Neue", Arial, sans-serif;
  }
  .sheet {
    position: relative; width: 1200px; height: 1000px;
    display: flex; flex-direction: column; align-items: center; justify-content: center; gap: 60px;
  }
  .card {
    position: relative; width: 700px; height: 400px;
    border-radius: 28px; overflow: hidden;
    box-shadow: 0 10px 30px rgba(0,0,0,.18);
  }

  /* Front */
  .card-front {
    background: radial-gradient(ellipse at 55% 30%, var(--card-glow) 0%, var(--card-black) 70%);
  }
  .brand {
    position: absolute; left: 44px; top: 122px;
    display: flex; align-items: center; gap: 14px;
  }
  .brand-square { width: 30px; height: 30px; background: var(--ink-white); }
  .brand-name {
    color: var(--ink-white); font-weight: 500; font-size: 30px;
    letter-spacing: 1px; text-transform: uppercase;
  }
  .contact {
    position: absolute; right: 40px; top: 40px; text-align: right;
    color: var(--ink-white);
  }
  .contact-name, .contact-title { font-size: 34px; font-weight: 500; line-height: 1.15; }
  .contact-line {
    display: flex; align-items: center; justify-content: flex-end; gap: 10px;
    font-size: 22px; color: var(--ink-soft); margin-top: 6px;
  }
  .contact-line svg { width: 18px; height: 18px; flex: none; }
  .card-front .band { position: absolute; inset: 0; }
  .band-text { font-size: 20px; fill: var(--ink-white); letter-spacing: .5px; }
  .email-text { font-size: 22px; fill: var(--ink-muted); }

  /* Back */
  .card-back { background: var(--card-black); padding: 14px; }
  .map-area {
    position: relative; width: 100%; height: 100%; border-radius: 20px;
    background: linear-gradient(160deg, var(--map-fill) 0%, var(--map-fill-deep) 100%);
  }
  .location {
    position: absolute; left: 50%; top: 50%; transform: translate(-50%, -50%);
    display: flex; align-items: center; gap: 12px;
    padding: 10px 18px; border-radius: 10px;
    background: rgba(255,255,255,.75);
    color: var(--marker);
  }
  .location svg { width: 26px; height: 34px; flex: none; }
  .location-name { font-size: 20px; font-weight: 500; line-height: 1.2; }
  .location-address { font-size: 17px; color: var(--ink-map); line-height: 1.3; }
</style>
</head>
<body>
<main class="sheet">
  <section class="card card-front">
    <div class="brand">
      <span class="brand-square"></span>
      <span class="brand-name">The Marble Depot</span>
    </div>

    <div class="contact">
      <p class="contact-name">Carl Whitmore</p>
      <p class="contact-title">Owner</p>
      <p class="contact-line">214-555-0182
        <svg viewBox="0 0 20 20" aria-hidden="true"><circle cx="10" cy="10" r="9" fill="#fff"/><path d="M7 5h2l1 3-1.5 1a7 7 0 0 0 3 3l1-1.5 3 1v2a1.5 1.5 0 0 1-1.5 1.5A9 9 0 0 1 5.5 6.5 1.5 1.5 0 0 1 7 5z" fill="#111"/></svg>
      </p>
      <p class="contact-line">MDPlanoworks.com
        <svg viewBox="0 0 20 20" aria-hidden="true"><circle cx="10" cy="10" r="9" fill="#fff"/><circle cx="10" cy="10" r="5" fill="none" stroke="#111" stroke-width="1.5"/><path d="M5 10h10M10 5v10" stroke="#111" stroke-width="1.2"/></svg>
      </p>
    </div>

    <svg class="band" viewBox="0 0 700 400" aria-hidden="true">
      <defs>
        <linearGradient id="bandFill" x1="0" y1="0" x2="0" y2="1">
          <stop offset="0" stop-color="#b9bbbd"/>
          <stop offset="1" stop-color="#8e9092"/>
        </linearGradient>
        <path id="emailPath" d="M150 318 C330 306 480 272 680 218"/>
        <path id="bandPath" d="M0 384 C230 382 445 340 700 272"/>
      </defs>
      <path d="M0 350 C220 350 440 306 700 238 L700 292 C450 358 240 400 0 402 Z" fill="url(#bandFill)"/>
      <path d="M0 350 C220 350 440 306 700 238" fill="none" stroke="#dcdddd" stroke-width="2"/>
      <text class="email-text"><textPath href="#emailPath" startOffset="100%" text-anchor="end">Carl.Whitmore@MDPlanoworks.com</textPath></text>
      <text class="band-text"><textPath href="#bandPath" startOffset="52%" text-anchor="middle">Install and supply Granite Counter tops</textPath></text>
    </svg>
  </section>

  <section class="card card-back">
    <div class="map-area" role="img" aria-label="Mapvista street map showing the store location at 10483 Pelham Ridge Blvd., Dallas, Texas 75220">
      <div class="location">
        <svg viewBox="0 0 26 34" aria-hidden="true"><path d="M13 1C6.4 1 1 6.2 1 12.6 1 21.5 13 33 13 33s12-11.5 12-20.4C25 6.2 19.6 1 13 1z" fill="#2a2a2a"/><circle cx="13" cy="12.5" r="4.5" fill="#fff"/></svg>
        <div>
          <p class="location-name">The Marble Depot</p>
          <p class="location-address">10483 Pelham Ridge Blvd., Dallas, Texas 75220</p>
        </div>
      </div>
    </div>
  </section>
</main>
</body>
</html>
```